Stationary Design Letterhead and Envelope

Artist should provide Letterhead and envelop stationary designs

Info for stationary:
Fernhallow Outdoor Advertising
4873 Quarry Rd. 915 N. PO BOX 528617
Austin, TX 78519

Dale Fernhallow
President
555-862-1907
dale@fernhallowsigns.example
fernhallowsigns.example

Target Market(s)

clients

Colors
0054AA
0677BA
7BADD7
CADEEF
E8F1F8

Requirements
Must have
• high quality unique eye catching and dynamic

```html
<!DOCTYPE html>
<html lang="en">
<head>
<meta charset="utf-8">
<title>Fernhallow Outdoor Advertising – Stationery</title>
<link href="https://fonts.googleapis.com/css2?family=Arimo:wght@400;700&display=swap" rel="stylesheet">
<style>
  :root{
    --blue:#0067a0;
    --blue-deep:#0054aa;
    --ink:#1a1a1a;
    --paper:#f2f2f2;
    --stage:#9c9c9c;
    --black:#0c0c0c;
    --white:#ffffff;
  }
  *{box-sizing:border-box;margin:0;padding:0}
  html,body{width:1200px;height:1011px;overflow:hidden}
  body{background:var(--stage);font-family:"Arimo",Arial,sans-serif;color:var(--ink);position:relative}

  .sheet{position:absolute;background:var(--paper);box-shadow:0 1px 4px rgba(0,0,0,.25);overflow:hidden}

  /* wordmark stand-in */
  .wordmark{position:absolute;font-family:"Arimo",Arial,sans-serif;font-weight:700;letter-spacing:.5px;line-height:1;white-space:nowrap}
  .wordmark--dark{color:var(--ink)}
  .wordmark--light{color:var(--white)}

  /* letterhead */
  .letterhead{left:85px;top:149px;width:508px;height:719px}
  .letterhead .wordmark{left:41px;top:38px;font-size:20px}
  .sender{position:absolute;left:318px;top:32px;font-size:8.2px;line-height:10.4px}
  .sender__name{border-left:3px solid var(--blue);padding-left:7px;margin-left:1px;margin-bottom:8px}
  .sender__name strong{display:block;color:var(--blue);font-size:10.4px;line-height:12px}
  .sender__name span{display:block;font-size:8.2px;line-height:10px}
  .sender__address{margin-bottom:4px}
  .contact-line{display:flex;align-items:center;gap:4px}
  .contact-line svg{width:7px;height:7px;flex:none}

  .letter{position:absolute;left:54px;top:170px;width:401px;font-size:8.2px;line-height:12px}
  .letter__date{margin-bottom:12px}
  .letter__recipient{margin-bottom:24px}
  .letter__salutation{margin-bottom:12px}
  .letter p.body{text-align:justify;margin-bottom:12px}
  .letter__closing{margin-top:36px}
  .signature{display:block;width:115px;height:18px;margin-top:6px;background:linear-gradient(90deg,rgba(26,26,26,.18),rgba(26,26,26,.06));border-radius:2px}

  .footer-band{position:absolute;left:0;right:0;height:16px;background:var(--blue)}
  .footer-band__mark{position:absolute;right:0;top:0;height:100%;width:140px;background:var(--black)}
  .footer-band .wordmark{top:2px;font-size:13px}

  .letterhead .footer-band{top:690px}
  .letterhead .footer-band .wordmark{right:38px}

  /* envelope back */
  .envelope-back{left:632px;top:351px;width:509px;height:241px}
  .envelope-back__flap{position:absolute;left:0;top:0;width:509px;height:80px}
  .envelope-back .wordmark{left:0;right:0;top:27px;text-align:center;font-size:18px}
  .envelope-back__fold{position:absolute;left:0;top:0;width:509px;height:241px}

  /* envelope front */
  .envelope-front{left:632px;top:626px;width:509px;height:242px}
  .envelope-front .wordmark{left:44px;top:30px;font-size:18px}
  .envelope-front .sender{left:43px;top:140px;font-size:7.4px;line-height:9.8px}
  .envelope-front .footer-band{top:213px}
  .envelope-front .footer-band .wordmark{right:34px}
</style>
</head>
<body>

<section class="sheet letterhead" aria-label="Letterhead">
  <div class="wordmark wordmark--dark">FERNHALLOW</div>

  <div class="sender">
    <div class="sender__name"><strong>Dale Fernhallow</strong><span>President</span></div>
    <div class="sender__address">Fernhallow Outdoor Advertising<br>4873 Quarry Rd. 915 N. PO BOX 528617<br>Austin, TX 78519</div>
    <div class="contact-line"><svg viewBox="0 0 10 10"><path d="M2 1l2 2-1 1.3c.6 1.2 1.5 2.1 2.7 2.7L7 6l2 2-1.5 1.5C4.5 9 1 5.5.5 2.5z" fill="var(--blue)"/></svg>555-862-1907</div>
    <div class="contact-line"><svg viewBox="0 0 10 10"><rect x=".5" y="2" width="9" height="6" fill="var(--blue)"/><path d="M.5 2l4.5 3.5L9.5 2" stroke="#fff" fill="none" stroke-width=".8"/></svg>dale@fernhallowsigns.example</div>
    <div class="contact-line"><svg viewBox="0 0 10 10"><circle cx="5" cy="5" r="4.3" fill="none" stroke="var(--blue)" stroke-width="1"/><path d="M.7 5h8.6M5 .7c-2.4 2.6-2.4 6 0 8.6M5 .7c2.4 2.6 2.4 6 0 8.6" stroke="var(--blue)" fill="none" stroke-width=".8"/></svg>www.fernhallowsigns.example</div>
  </div>

  <div class="letter">
    <p class="letter__date">01 January 2050</p>
    <p class="letter__recipient">Company (Pvt) Ltd.<br>PO Box 3355 Mainville St<br>Sample City Country 3355</p>
    <p class="letter__salutation">Dear Martin Okafor,</p>
    <p class="body">Lorem ipsum dolor sit amet, consectetuer adipiscing elit, sed diam nonummy nibh euismod tincidunt ut laoreet dolore magna aliquam erat volutpat. Ut wisi enim ad minim veniam, quis nostrud exerci tation ullamcorper suscipit lobortis nisl ut aliquip ex ea commodo consequat. Duis dolore te feugait nulla facilisi. Nam liber tempor cum soluta nobis eleifend option congue nihil imperdiet doming id quod mazim placerat facer possim assum. Lorem ipsum dolor sit amet, consectetuer adipiscing elit, sed diam nonummy nibh euismod tincidunt ut laoreet dolore magna aliquam erat volutpat. Ut wisi enim ad minim veniam, quis nostrud exerci tation ullamcorper suscipit lobortis nisl ut aliquip ex ea commodo consequat.</p>
    <p class="body">Consectetuer adipiscing elit, sed diam nonummy nibh euismod tincidunt ut laoreet dolore magna aliquam erat volutpat. Ut wisi enim ad minim veniam, quis nostrud exerci tation ullamcorper suscipit lobortis nisl ut aliquip ex ea commodo consequat. Consectetuer adipiscing elit, sed diam nonummy nibh euismod tincidunt ut laoreet dolore magna aliquam erat volutpat. Ut wisi enim ad minim veniam, quis nostrud exerci tation ullamcorper suscipit lobortis nisl ut aliquip ex ea commodo consequat.</p>
    <p class="body">Consectetuer adipiscing elit, sed diam nonummy nibh euismod tincidunt ut laoreet dolore magna aliquam erat volutpat. Ut wisi enim ad minim veniam, quis nostrud exerci tation ullamcorper suscipit lobortis nisl ut aliquip ex ea commodo consequat. Consectetuer adipiscing elit, sed diam nonummy nibh euismod tincidunt ut laoreet dolore magna aliquam erat volutpat. Ut wisi enim ad minim veniam, quis nostrud exerci tation ullamcorper suscipit lobortis nisl ut aliquip ex ea commodo consequat.</p>
    <p class="letter__closing">Sincerely Yours</p>
    <span class="signature" role="img" aria-label="Handwritten signature of Harold Brenning"></span>
  </div>

  <div class="footer-band">
    <div class="footer-band__mark"></div>
    <div class="wordmark wordmark--light">FERNHALLOW</div>
  </div>
</section>

<section class="sheet envelope-back" aria-label="Envelope back">
  <svg class="envelope-back__fold" viewBox="0 0 509 241" aria-hidden="true">
    <path d="M10 62 L12 234 M499 62 L497 234" stroke="#d8d8d8" fill="none" stroke-width="1"/>
  </svg>
  <svg class="envelope-back__flap" viewBox="0 0 509 80" aria-hidden="true">
    <path d="M0 0 H509 L493 70 Q490 79 480 79 H29 Q19 79 16 70 Z" fill="var(--blue)"/>
  </svg>
  <div class="wordmark wordmark--light">FERNHALLOW</div>
</section>

<section class="sheet envelope-front" aria-label="Envelope front">
  <div class="wordmark wordmark--dark">FERNHALLOW</div>
  <div class="sender">
    <div class="sender__address">Fernhallow Outdoor Advertising<br>4873 Quarry Rd. 915 N. PO BOX 528617<br>Austin, TX 78519</div>
    <div class="contact-line"><svg viewBox="0 0 10 10"><path d="M2 1l2 2-1 1.3c.6 1.2 1.5 2.1 2.7 2.7L7 6l2 2-1.5 1.5C4.5 9 1 5.5.5 2.5z" fill="var(--blue)"/></svg>555-862-1907</div>
    <div class="contact-line"><svg viewBox="0 0 10 10"><rect x=".5" y="2" width="9" height="6" fill="var(--blue)"/><path d="M.5 2l4.5 3.5L9.5 2" stroke="#fff" fill="none" stroke-width=".8"/></svg>dale@fernhallowsigns.example</div>
    <div class="contact-line"><svg viewBox="0 0 10 10"><circle cx="5" cy="5" r="4.3" fill="none" stroke="var(--blue)" stroke-width="1"/><path d="M.7 5h8.6M5 .7c-2.4 2.6-2.4 6 0 8.6M5 .7c2.4 2.6 2.4 6 0 8.6" stroke="var(--blue)" fill="none" stroke-width=".8"/></svg>www.fernhallowsigns.example</div>
  </div>
  <div class="footer-band">
    <div class="footer-band__mark"></div>
    <div class="wordmark wordmark--light">FERNHALLOW</div>
  </div>
</section>

</body>
</html>
```